WEBSITE DESIGN - www.brindolux.com

We need a professional and modern looking website for our business. The current website was only made tentatively and can be viewed (we expect a website MUCH better than this). It needs to be simple and non-cluttered yet look modern and sophisticated. It needs to be very easy to navigate as our tarket market is people over the age of 45. Our logo is attached below and this should be incorporated plus the colours/theme should match this. We don't mind purchasing images online if your design includes these and we like it.

Any other specific questions please enquire as we want to hear them.

Target Market(s)

over 45 age english speaking westerners

Industry/Entity Type

Business

Number of Pages Required

1 page

Requirements
Must have
• -our logo (attached).
• -page tabs as those described (tabs.. but not necessarily each of these pages completed as well although this would be nice).
• -social media logos
• Pages should include: homepage, services, pricing, about us, contact us. There should also be a payments page designed which would link with the other pages but there would be no tab for this.

```html
<!DOCTYPE html>
<html lang="en">
<head>
<meta charset="utf-8">
<title>Brindolux – Computer Solutions</title>
<link href="https://fonts.googleapis.com/css2?family=Bitter:wght@400;500;600&family=Open+Sans:wght@400;600;700&display=swap" rel="stylesheet">
<style>
:root{
  --gold:#f2bc3e;
  --gold-soft:#f8d98a;
  --brown:#9b6a0c;
  --brown-dark:#7d5408;
  --ink:#333333;
  --muted:#777777;
  --light:#f4f4f4;
  --white:#ffffff;
  --dark:#4b4946;
}
*{box-sizing:border-box;margin:0;padding:0}
html,body{width:1200px;height:3158px;overflow:hidden}
body{font-family:"Open Sans",Arial,sans-serif;color:var(--ink);background:var(--white);position:relative}
.serif{font-family:"Bitter",Georgia,serif}
section,header,nav,footer{position:absolute;left:0;width:1200px}

/* header */
.site-header{top:0;height:110px;background:var(--white)}
.brand{position:absolute;left:75px;top:22px;display:flex;align-items:center;gap:12px}
.brand-mark{width:40px;height:40px;background:var(--brown);border-radius:50%}
.brand-name{font-family:"Bitter",Georgia,serif;font-size:30px;color:var(--ink);line-height:1}
.brand-tag{font-size:10px;letter-spacing:2px;color:var(--muted);margin-top:4px}
.contact-bar{position:absolute;right:75px;top:36px;display:flex;align-items:center;gap:12px;font-size:18px;font-weight:600}
.phone-icon{width:32px;height:32px;border-radius:50%;background:var(--gold);display:flex;align-items:center;justify-content:center}
.social{display:flex;gap:12px;margin-left:12px}
.social span{width:24px;height:24px;background:var(--gold);border-radius:3px}

/* nav */
.main-nav{top:110px;height:52px;background:var(--brown)}
.main-nav ul{list-style:none;display:flex;margin-left:75px;height:52px}
.main-nav li{color:var(--white);font-size:13px;padding:0 33px;line-height:52px;text-transform:uppercase;letter-spacing:.5px}
.main-nav li.active{background:var(--gold)}
.search{position:absolute;right:75px;top:15px}

/* hero */
.hero{top:162px;height:418px;background:linear-gradient(100deg,#3e3a36 0%,#6d6254 35%,#b29b78 65%,#e0c48d 100%)}
.hero-arrow{position:absolute;top:190px}
.cta-band{top:580px;height:103px;background:var(--gold)}
.cta-band h2{position:absolute;left:75px;top:20px;font-family:"Bitter",Georgia,serif;font-size:29px;color:var(--white);font-weight:600}
.cta-band p{position:absolute;left:75px;top:63px;font-size:14px;color:var(--white)}
.btn{display:inline-block;background:var(--brown);color:var(--white);text-transform:uppercase;font-size:12px;font-weight:600}
.cta-band .btn{position:absolute;right:77px;top:30px;width:197px;height:44px;line-height:44px;text-align:center;text-transform:none;font-family:"Bitter",Georgia,serif;font-size:17px;font-weight:400}

/* services */
.services{top:683px;height:532px;background:var(--light)}
.section-title{font-family:"Bitter",Georgia,serif;font-size:30px;text-align:center;font-weight:500;color:var(--ink)}
.section-lead{font-size:12.5px;color:var(--muted);text-align:center;line-height:20px;width:720px;margin:0 auto}
.services .section-title{margin-top:52px}
.services .section-lead{margin-top:14px}
.service-card{position:absolute;top:169px;width:242px;height:303px;background:var(--white);text-align:center;box-shadow:0 14px 10px -10px rgba(0,0,0,.25)}
.service-card h3{font-family:"Bitter",Georgia,serif;font-size:16px;color:var(--brown);font-weight:500;margin-top:26px;text-transform:uppercase}
.icon-ring{width:84px;height:84px;border:2px solid var(--brown);border-radius:50%;margin:26px auto 0;display:flex;align-items:center;justify-content:center}
.service-card p{font-size:12.5px;color:var(--muted);line-height:19px;margin:26px 24px 0;height:56px}
.service-card .btn{margin-top:14px;width:126px;height:36px;line-height:36px}

/* welcome */
.welcome{top:1215px;height:277px;text-align:center}
.welcome h2{margin-top:55px}
.welcome h2 em{font-style:normal;color:var(--brown)}
.welcome p{font-size:12.5px;color:var(--muted);line-height:22px;width:1055px;margin:18px auto 0}
.welcome .btn{margin-top:26px;width:128px;height:36px;line-height:36px}

/* pricing */
.pricing{top:1492px;height:680px;background:linear-gradient(180deg,#55524e,#3f3d3a)}
.pricing .kicker{text-align:center;color:var(--white);font-family:"Bitter",Georgia,serif;font-size:22px;margin-top:50px}
.pricing .section-title{color:var(--gold);font-size:28px;margin-top:4px}
.plan{position:absolute;top:143px;width:331px;height:481px;background:var(--white);text-align:center}
.plan-head{height:48px;line-height:48px;background:var(--gold);color:var(--white);font-family:"Bitter",Georgia,serif;font-size:20px}
.plan-price{height:62px;background:#faf0d4;font-family:"Bitter",Georgia,serif;font-size:20px;color:var(--ink);padding-top:14px}
.plan.featured .plan-price{background:var(--gold-soft)}
.plan-term{width:74px;height:74px;border-radius:50%;background:var(--brown);border:4px solid var(--white);color:var(--white);margin:-30px auto 0;position:relative;padding-top:10px}
.plan-term b{display:block;font-family:"Bitter",Georgia,serif;font-size:26px;font-weight:500;line-height:28px}
.plan-term small{font-size:12px}
.plan-note{font-size:12px;color:var(--muted);line-height:19px;margin:14px 34px 0}
.plan ul{list-style:none;margin:12px 26px 0}
.plan li{font-size:12px;border-bottom:1px solid #e6e6e6;padding:8px 0}
.plan li:last-child{border:none}
.plan-terms{font-family:"Bitter",Georgia,serif;font-size:14px;color:var(--brown);margin-top:12px;display:flex;align-items:center;justify-content:center;gap:12px}
.plan-terms i{width:13px;height:13px;border:1px solid #cccccc;display:inline-block;margin-left:-28px;margin-right:14px}
.plan .btn{margin-top:18px;width:154px;height:42px;line-height:42px}

/* testimonials */
.testimonials{top:2172px;height:398px;background:var(--light)}
.testimonials .section-title{margin-top:42px;font-size:28px}
.quote{position:absolute;top:123px;width:480px;height:200px;background:var(--white);text-align:center;box-shadow:0 14px 10px -10px rgba(0,0,0,.2)}
.quote svg.qmark{margin-top:-28px}
.quote p{font-size:12.5px;font-style:italic;color:var(--muted);line-height:19px;margin:14px 40px 0}
.author{display:flex;justify-content:center;align-items:center;gap:10px;margin-top:16px;text-align:left}
.avatar{width:50px;height:50px;border-radius:50%;background:linear-gradient(135deg,#c9a47a,#7a5a3e);border:2px solid var(--gold)}
.author b{display:block;font-size:13px;color:var(--brown);font-weight:600}
.author small{font-size:12px;color:#aaaaaa;font-style:italic}
.dots{position:absolute;top:348px;left:588px;display:flex;gap:6px}
.dots span{width:8px;height:8px;border-radius:50%;background:#cccccc}
.dots span:first-child{background:var(--brown)}

/* stats */
.stats{top:2570px;height:282px;background:linear-gradient(135deg,#f4c552,#eeb22e)}
.stat{position:absolute;top:52px;width:180px;height:180px;text-align:center;color:var(--white)}
.stat svg{position:absolute;left:0;top:0}
.stat b{display:block;font-family:"Bitter",Georgia,serif;font-size:32px;font-weight:500;margin-top:58px;position:relative}
.stat small{display:block;font-family:"Bitter",Georgia,serif;font-size:11px;text-transform:uppercase;letter-spacing:.5px;position:relative;line-height:14px}

/* partners */
.partners{top:2852px;height:178px;background:var(--white)}
.partner{position:absolute;top:44px;width:150px;height:94px;border:1px solid #dddddd;display:flex;align-items:center;justify-content:center}
.partner span{width:70px;height:34px;background:#d4d4d4;border-radius:4px}

/* footer */
.site-footer{top:3030px;height:128px;background:var(--brown);color:var(--white)}
.footer-links{position:absolute;left:75px;top:45px;font-size:11.5px;text-transform:uppercase}
.footer-links span{margin:0 10px}
.footer-copy{position:absolute;left:75px;top:74px;font-size:12px}
.footer-social{position:absolute;right:75px;top:50px;display:flex;align-items:center;gap:12px;font-size:11px;text-transform:uppercase}
.footer-social i{width:26px;height:26px;background:var(--white);border-radius:3px;display:inline-block}
</style>
</head>
<body>

<header class="site-header">
  <div class="brand">
    <span class="brand-mark"></span>
    <div>
      <div class="brand-name">Brindolux</div>
      <div class="brand-tag">COMPUTER SOLUTIONS</div>
    </div>
  </div>
  <div class="contact-bar">
    <span class="phone-icon"><svg width="16" height="16" viewBox="0 0 24 24"><path fill="#fff" d="M6.6 10.8a15 15 0 0 0 6.6 6.6l2.2-2.2c.3-.3.7-.4 1-.2 1.1.4 2.3.6 3.6.6.6 0 1 .4 1 1V20c0 .6-.4 1-1 1A17 17 0 0 1 3 4c0-.6.4-1 1-1h3.5c.6 0 1 .4 1 1 0 1.3.2 2.5.6 3.6.1.3 0 .7-.2 1z"/></svg></span>
    +44 (0) 1632 960418
    <div class="social"><span></span><span></span><span></span></div>
  </div>
</header>

<nav class="main-nav">
  <ul>
    <li class="active">Home</li><li>About Us</li><li>Services</li><li>Testimonial</li><li>Contact Us</li>
  </ul>
  <svg class="search" width="22" height="22" viewBox="0 0 24 24"><circle cx="10" cy="10" r="7" fill="none" stroke="#fff" stroke-width="3"/><path d="M15 15l6 6" stroke="#fff" stroke-width="3" stroke-linecap="round"/></svg>
</nav>

<section class="hero" role="img" aria-label="Photo of a person in a tweed jacket using a tablet">
  <svg class="hero-arrow" style="left:60px" width="24" height="40" viewBox="0 0 24 40"><path d="M18 6L6 20l12 14" fill="none" stroke="#fff" stroke-width="3"/></svg>
  <svg class="hero-arrow" style="right:60px" width="24" height="40" viewBox="0 0 24 40"><path d="M6 6l12 14L6 34" fill="none" stroke="#fff" stroke-width="3" opacity=".6"/></svg>
</section>

<section class="cta-band">
  <h2>Call us Today for Instant Tech Support NOW!</h2>
  <p>sed ut perspiciatis unde omnis iste natus error sit voluptatem accusantium doloremque lauda</p>
  <span class="btn">Contact Us Now</span>
</section>

<section class="services">
  <h2 class="section-title">Best Services</h2>
  <p class="section-lead">Sed ut perspiciatis unde omnis iste natus error sit voluptatem accusantium doloremque laudantium, totam rem aperiam eaque ipsa quae ab illo inventore veritatis et quasi architecto beatae vitae.</p>

  <div class="service-card" style="left:75px">
    <h3>Tech Support</h3>
    <div class="icon-ring"><svg width="36" height="36" viewBox="0 0 24 24"><circle cx="12" cy="8" r="4.5" fill="#9b6a0c"/><path d="M3 22c0-5 4-8 9-8s9 3 9 8z" fill="#9b6a0c"/></svg></div>
    <p>We make technology easier for you with instant support</p>
    <span class="btn">Read More</span>
  </div>
  <div class="service-card" style="left:344px">
    <h3>Downloads</h3>
    <div class="icon-ring"><svg width="36" height="36" viewBox="0 0 24 24"><path d="M12 2v12M7 9l5 5 5-5" fill="none" stroke="#9b6a0c" stroke-width="2.6"/><path d="M3 15v6h18v-6" fill="none" stroke="#9b6a0c" stroke-width="2.6"/></svg></div>
    <p>The best apps to optimize &amp; secure your digital devices.</p>
    <span class="btn">Read More</span>
  </div>
  <div class="service-card" style="left:614px">
    <h3>Web Design</h3>
    <div class="icon-ring"><svg width="36" height="36" viewBox="0 0 24 24"><circle cx="12" cy="12" r="10" fill="#9b6a0c"/><path d="M2 12h20M12 2c3 3 3 17 0 20M12 2c-3 3-3 17 0 20" fill="none" stroke="#fff" stroke-width="1.3"/></svg></div>
    <p>We understand that every business owner has his own way of showcasing products</p>
    <span class="btn">Read More</span>
  </div>
  <div class="service-card" style="left:882px">
    <h3>The Urgency</h3>
    <div class="icon-ring"><svg width="36" height="36" viewBox="0 0 24 24"><circle cx="12" cy="12" r="9.5" fill="none" stroke="#9b6a0c" stroke-width="2.4"/><path d="M12 6v6l4 2" fill="none" stroke="#9b6a0c" stroke-width="2.4"/></svg></div>
    <p>We believe in careful planning for you.</p>
    <span class="btn">Read More</span>
  </div>
</section>

<section class="welcome">
  <h2 class="section-title">Welcome to <em>Brindolux</em></h2>
  <p>Sed ut perspiciatis unde omnis iste natus error sit voluptatem accusantium doloremque laudantium, totam rem aperiam, eaque ipsa quae ab illo inventore veritatis et quasi architecto beatae vitae dicta sunt explicabo. Nemo enim ipsam voluptatem quia voluptas sit aspernatur aut odit aut fugit, sed quia consequuntur magni dolores eos qui ratione voluptatem sequi nesciunt. Neque porro quisquam est</p>
  <span class="btn">Read More</span>
</section>

<section class="pricing">
  <div class="kicker">BEST PRICES</div>
  <h2 class="section-title">Our Affordable Prices</h2>

  <div class="plan" style="left:75px">
    <div class="plan-head">Quick Fix</div>
    <div class="plan-price">NZD 95, &nbsp;USD 60*, &nbsp;GBP 40*</div>
    <div class="plan-term"><b>01</b><small>month</small></div>
    <p class="plan-note">*The price advertised might not be the same price charged to the credit card account due to exchange rate fluctuations.</p>
    <ul><li>1 Month Tech Support</li><li>For 1 Computer</li><li>24X7 Availability</li></ul>
    <div class="plan-terms"><i></i>I agree to the Terms &amp; Conditions</div>
    <span class="btn">Order Now &#8853;</span>
  </div>
  <div class="plan" style="left:434px">
    <div class="plan-head">Starter</div>
    <div class="plan-price">NZD 95, &nbsp;USD 60*, &nbsp;GBP 40*</div>
    <div class="plan-term"><b>06</b><small>month</small></div>
    <p class="plan-note">*The price advertised might not be the same price charged to the credit card account due to exchange rate fluctuations.</p>
    <ul><li>1 Month Tech Support</li><li>For 1 Computer</li><li>24X7 Availability</li></ul>
    <div class="plan-terms"><i></i>I agree to the Terms &amp; Conditions</div>
    <span class="btn">Order Now &#8853;</span>
  </div>
  <div class="plan featured" style="left:793px">
    <div class="plan-head">Advance</div>
    <div class="plan-price">NZD 95, &nbsp;USD 60*, &nbsp;GBP 40*</div>
    <div class="plan-term"><b>01</b><small>Year</small></div>
    <p class="plan-note">*The price advertised might not be the same price charged to the credit card account due to exchange rate fluctuations.</p>
    <ul><li>1 Month Tech Support</li><li>For 1 Computer</li><li>24X7 Availability</li></ul>
    <div class="plan-terms"><i></i>I agree to the Terms &amp; Conditions</div>
    <span class="btn">Order Now &#8853;</span>
  </div>
</section>

<section class="testimonials">
  <h2 class="section-title">What Our Client Say’s</h2>
  <div class="quote" style="left:98px">
    <svg class="qmark" width="64" height="50" viewBox="0 0 64 50"><path d="M4 46V28C4 12 12 4 26 2v8c-7 2-10 6-10 14h10v22zM36 46V28c0-16 8-24 22-26v8c-7 2-10 6-10 14h10v22z" fill="#9b6a0c"/></svg>
    <p>veritatis et quasi architecto beatae vitae dicta sunt explicabo. Nemo enim ipsam voluptatem quia voluptas sit aspernatur aut odit aut fugit sed quia consequuntur magni dolores eos.</p>
    <div class="author"><span class="avatar" role="img" aria-label="Client portrait"></span><div><b>By Della Ravenwood</b><small>city, location</small></div></div>
  </div>
  <div class="quote" style="left:620px">
    <svg class="qmark" width="64" height="50" viewBox="0 0 64 50"><path d="M4 46V28C4 12 12 4 26 2v8c-7 2-10 6-10 14h10v22zM36 46V28c0-16 8-24 22-26v8c-7 2-10 6-10 14h10v22z" fill="#9b6a0c"/></svg>
    <p>veritatis et quasi architecto beatae vitae dicta sunt explicabo. Nemo enim ipsam voluptatem quia voluptas sit aspernatur aut odit aut fugit sed quia consequuntur magni dolores eos.</p>
    <div class="author"><span class="avatar" role="img" aria-label="Client portrait"></span><div><b>By Della Ravenwood</b><small>city, location</small></div></div>
  </div>
  <div class="dots"><span></span><span></span></div>
</section>

<section class="stats">
  <div class="stat" style="left:75px"><svg width="180" height="180"><circle cx="90" cy="90" r="84" fill="none" stroke="#a06e10" stroke-width="9"/><circle cx="90" cy="90" r="84" fill="none" stroke="#fff" stroke-width="9" stroke-dasharray="26 502" transform="rotate(-90 90 90)"/></svg><b>95%</b><small>Awesomeness</small></div>
  <div class="stat" style="left:254px"><svg width="180" height="180"><circle cx="90" cy="90" r="84" fill="none" stroke="#a06e10" stroke-width="9"/></svg><b>100%</b><small>Support</small></div>
  <div class="stat" style="left:433px"><svg width="180" height="180"><circle cx="90" cy="90" r="84" fill="none" stroke="#a06e10" stroke-width="9"/><circle cx="90" cy="90" r="84" fill="none" stroke="#fff" stroke-width="9" stroke-dasharray="16 512" transform="rotate(-90 90 90)"/></svg><b>97%</b><small>Software<br>Installation</small></div>
  <div class="stat" style="left:612px"><svg width="180" height="180"><circle cx="90" cy="90" r="84" fill="none" stroke="#a06e10" stroke-width="9"/><circle cx="90" cy="90" r="84" fill="none" stroke="#fff" stroke-width="9" stroke-dasharray="37 491" transform="rotate(-90 90 90)"/></svg><b>93%</b><small>Virus Removal</small></div>
  <div class="stat" style="left:791px"><svg width="180" height="180"><circle cx="90" cy="90" r="84" fill="none" stroke="#a06e10" stroke-width="9"/><circle cx="90" cy="90" r="84" fill="none" stroke="#fff" stroke-width="9" stroke-dasharray="11 517" transform="rotate(-90 90 90)"/></svg><b>98%</b><small>Flexibility</small></div>
  <div class="stat" style="left:970px"><svg width="180" height="180"><circle cx="90" cy="90" r="84" fill="none" stroke="#a06e10" stroke-width="9"/><circle cx="90" cy="90" r="84" fill="none" stroke="#fff" stroke-width="9" stroke-dasharray="32 496" transform="rotate(-90 90 90)"/></svg><b>94%</b><small>System Setup</small></div>
</section>

<section class="partners">
  <div class="partner" style="left:75px"><span></span></div>
  <div class="partner" style="left:254px"><span></span></div>
  <div class="partner" style="left:433px"><span></span></div>
  <div class="partner" style="left:612px"><span></span></div>
  <div class="partner" style="left:791px"><span></span></div>
  <div class="partner" style="left:970px"><span></span></div>
</section>

<footer class="site-footer">
  <div class="footer-links">Home<span>|</span>About Us<span>|</span>Services<span>|</span>Testimonial<span>|</span>Contact Us</div>
  <div class="footer-copy">© 2016 Brindolux. All Rights Reserved.</div>
  <div class="footer-social">Get Social: <i></i><i></i><i></i></div>
</footer>

</body>
</html>
```